Business card for Financial Technology company

Hello! We'd like to create business cards for 4 members of our company. Our company is a financial technology business that provides funding for businesses. We want to give it a VC (venture captal) look and feel. Clean, fresh and minimal but with a flair of artistry. I'll include some samples of cards we like. It would be great if the back of the card was artistic (see sample files 1 and 2) and the front of the card was the business info. The name of the company is Corvana Capital.

```html
<!DOCTYPE html>
<html lang="en">
<head>
<meta charset="UTF-8">
<title>Corvana Capital – Business Card</title>
<link href="https://fonts.googleapis.com/css2?family=Inter:wght@400;700&display=swap" rel="stylesheet">
<style>
  :root {
    --backdrop: #c4c4c4;
    --card-white: #ffffff;
    --ink: #111111;
    --ink-soft: #333333;
    --ink-muted: #6b6b6b;
    --lime: #b5ec7c;
    --green: #0f9a4e;
    --teal: #2c6f86;
    --indigo: #4b4fa6;
    --lavender: #b8a6f2;
    --magenta: #d8087e;
    --coral: #f2586a;
    --amber: #f5a21e;
    --yellow: #ffd910;
  }
  * { margin: 0; padding: 0; box-sizing: border-box; }
  html, body {
    width: 1200px;
    height: 1200px;
    overflow: hidden;
    background: var(--backdrop);
    font-family: "Inter", sans-serif;
  }
  .canvas {
    position: relative;
    width: 1200px;
    height: 1200px;
  }
  .card {
    position: absolute;
    top: 226px;
    width: 436px;
    height: 746px;
  }
  .card-back {
    left: 124px;
    background: linear-gradient(180deg,
      var(--lime) 0%,
      var(--green) 18%,
      var(--teal) 34%,
      var(--indigo) 44%,
      var(--lavender) 56%,
      var(--magenta) 70%,
      var(--coral) 82%,
      var(--amber) 92%,
      var(--yellow) 100%);
  }
  .card-front {
    left: 620px;
    background: var(--card-white);
    text-align: center;
  }
  .brand {
    position: absolute;
    top: 242px;
    left: 0;
    width: 100%;
    display: flex;
    align-items: center;
    justify-content: center;
    gap: 12px;
  }
  .brand-mark {
    width: 26px;
    height: 26px;
    background: var(--magenta);
  }
  .brand-name {
    font-size: 34px;
    font-weight: 700;
    color: var(--ink);
    letter-spacing: -0.5px;
  }
  .person-name {
    position: absolute;
    top: 496px;
    width: 100%;
    font-size: 28px;
    font-weight: 700;
    color: var(--ink);
  }
  .person-title {
    position: absolute;
    top: 535px;
    width: 100%;
    font-size: 18px;
    font-weight: 400;
    color: var(--ink-soft);
  }
  .contact-list {
    position: absolute;
    top: 594px;
    width: 100%;
    list-style: none;
    font-size: 18px;
    line-height: 29.5px;
    color: var(--ink-muted);
  }
</style>
</head>
<body>
  <main class="canvas">
    <section class="card card-back" role="img" aria-label="Geometric triangle pattern in a rainbow gradient from lime green through blue, violet and magenta to yellow"></section>

    <section class="card card-front">
      <div class="brand">
        <span class="brand-mark"></span>
        <span class="brand-name">Corvana Capital</span>
      </div>
      <h1 class="person-name">Name Surname</h1>
      <p class="person-title">Title</p>
      <ul class="contact-list">
        <li>(888) 555-0142</li>
        <li>info@corvanacapital.com</li>
        <li>corvanacapital.com</li>
      </ul>
    </section>
  </main>
</body>
</html>
```